INNOVATIVE DESIGN NEEDED FOR FINANCIAL COMPANY

INTERNATIONAL FIRM IN HONG KONG NEEDS A MODERN BUSINESS CARD DESIGN. ONE SIDE ENGLISH OTHER SIDE IN CHINESE. WE ARE OPEN TO CHANGING FONTS AND COLOR. SHOULD BE A CARD THAT IS PROFESSIONAL DEALING WITH HIGH NET WORTH CLIENTELE. BOTH SIDES OF THE CARD WILL BE THE SAME, HOWEVER, THE WORDING ON ONE SIDE WILL BE ENGLISH AND THE OTHER SIDE IN CHINESE (CAN ASSIST IN THE LETTERING - CAN PROVIDE ONCE CARD DESIGN IS ACCEPTED.

Target Market(s)

Hong Kong/CHINA

Contact Information for Business Card

ATTRACTIVE MODERN

```html
<!DOCTYPE html>
<html lang="en">
<head>
<meta charset="utf-8">
<title>Birchwood Asset Management – Business Cards</title>
<link href="https://fonts.googleapis.com/css2?family=Noto+Sans+TC:wght@400;900&family=Roboto:wght@400;900&display=swap" rel="stylesheet">
<style>
  :root {
    --backdrop: #b3b1b2;
    --card-white: #ffffff;
    --card-black: #1e1e1e;
    --brand-green: #148a64;
    --ink-dark: #3a3a3a;
    --ink-light: #f2f2f2;
    --rule: #8a8a8a;
  }
  * { margin: 0; padding: 0; box-sizing: border-box; }
  html, body { width: 1200px; height: 895px; overflow: hidden; background: var(--backdrop); }
  .canvas { position: relative; width: 1200px; height: 895px; }
  .card {
    position: absolute; left: 250px; width: 700px; height: 400px;
    border-radius: 26px; overflow: hidden; background: var(--card-white);
    box-shadow: 0 6px 18px rgba(0,0,0,.25);
    font-family: "Roboto", "Noto Sans TC", sans-serif;
  }
  .card--chinese { top: 22px; }
  .card--english { top: 473px; }
  .card__bg { position: absolute; inset: 0; }
  .brand { position: absolute; left: 40px; top: 46px; display: flex; align-items: center; gap: 18px; }
  .brand__dot { width: 84px; height: 84px; border-radius: 50%; background: var(--brand-green); flex: none; }
  .brand__name { font-family: "Noto Sans TC", sans-serif; font-weight: 900; color: var(--ink-dark); line-height: 1.2; }
  .brand__name-zh { display: block; font-size: 34px; letter-spacing: 2px; }
  .brand__name-en { display: block; font-size: 16px; letter-spacing: 1px; }
  .holder { position: absolute; left: 46px; top: 280px; width: 270px; text-align: right; }
  .holder__name { color: var(--brand-green); font-weight: 900; font-size: 32px; line-height: 1.1; }
  .card--chinese .holder__name { font-family: "Noto Sans TC", sans-serif; font-weight: 400; letter-spacing: 2px; }
  .holder__title { color: var(--ink-light); font-size: 16px; margin-top: 4px; }
  .card--chinese .holder__title { font-family: "Noto Sans TC", sans-serif; }
  .divider { position: absolute; left: 336px; top: 252px; width: 1px; height: 84px; background: var(--rule); }
  .contacts { position: absolute; left: 356px; top: 250px; list-style: none; }
  .contacts li { display: flex; align-items: center; gap: 10px; color: var(--ink-light); font-size: 17px; height: 28px; white-space: nowrap; }
  .contacts .accent { color: var(--brand-green); }
  .contacts svg { width: 20px; height: 20px; flex: none; }
  .address { position: absolute; left: 46px; top: 358px; color: var(--ink-light); font-size: 17px; white-space: nowrap; }
  .address__label { color: var(--brand-green); }
</style>
</head>
<body>
<main class="canvas">

  <section class="card card--chinese" lang="zh-Hant">
    <svg class="card__bg" viewBox="0 0 700 400" aria-hidden="true">
      <path d="M0,252 C280,235 560,170 700,70 L700,400 L0,400Z" fill="var(--brand-green)"/>
      <path d="M0,264 C280,248 560,184 700,84 L700,400 L0,400Z" fill="var(--card-black)"/>
    </svg>
    <div class="brand">
      <span class="brand__dot"></span>
      <p class="brand__name"><span class="brand__name-zh">柏林資產管理有限公司</span><span class="brand__name-en">Birchwood Asset Management Ltd</span></p>
    </div>
    <div class="holder">
      <p class="holder__name">丹尼尔卡特</p>
      <p class="holder__title">管理伙伴</p>
    </div>
    <span class="divider"></span>
    <ul class="contacts">
      <li><svg viewBox="0 0 20 20"><circle cx="10" cy="10" r="10" fill="var(--brand-green)"/><path d="M6.5,5.5 l2,0 l1,2.5 -1.3,1 a6,6 0 0 0 2.8,2.8 l1,-1.3 2.5,1 0,2 a1,1 0 0 1 -1,1 a8,8 0 0 1 -8,-8 a1,1 0 0 1 1,-1z" fill="#fff"/></svg><span>000 000 0000</span></li>
      <li><svg viewBox="0 0 20 20"><circle cx="10" cy="10" r="10" fill="var(--brand-green)"/><rect x="5" y="6.5" width="10" height="7" fill="none" stroke="#fff" stroke-width="1.2"/><path d="M5,6.5 L10,10.5 L15,6.5" fill="none" stroke="#fff" stroke-width="1.2"/></svg><span>info@<span class="accent">birchwoodam</span>.com</span></li>
      <li><svg viewBox="0 0 20 20"><circle cx="10" cy="10" r="10" fill="var(--brand-green)"/><g fill="none" stroke="#fff" stroke-width="1.1"><circle cx="10" cy="10" r="5"/><ellipse cx="10" cy="10" rx="2.2" ry="5"/><path d="M5,10 H15"/></g></svg><span>www.<span class="accent">birchwoodam</span>.com</span></li>
    </ul>
    <p class="address"><span class="address__label">Address:</span> 240 rue des Érables, Ville Mont-Clair, QC H2X 3K9</p>
  </section>

  <section class="card card--english">
    <svg class="card__bg" viewBox="0 0 700 400" aria-hidden="true">
      <path d="M0,252 C280,235 560,170 700,70 L700,400 L0,400Z" fill="var(--brand-green)"/>
      <path d="M0,264 C280,248 560,184 700,84 L700,400 L0,400Z" fill="var(--card-black)"/>
    </svg>
    <div class="brand">
      <span class="brand__dot"></span>
      <p class="brand__name"><span class="brand__name-zh" lang="zh-Hant">柏林資產管理有限公司</span><span class="brand__name-en">Birchwood Asset Management Ltd</span></p>
    </div>
    <div class="holder">
      <p class="holder__name">Daniel Carter</p>
      <p class="holder__title">Managing Partner</p>
    </div>
    <span class="divider"></span>
    <ul class="contacts">
      <li><svg viewBox="0 0 20 20"><circle cx="10" cy="10" r="10" fill="var(--brand-green)"/><path d="M6.5,5.5 l2,0 l1,2.5 -1.3,1 a6,6 0 0 0 2.8,2.8 l1,-1.3 2.5,1 0,2 a1,1 0 0 1 -1,1 a8,8 0 0 1 -8,-8 a1,1 0 0 1 1,-1z" fill="#fff"/></svg><span>000 000 0000</span></li>
      <li><svg viewBox="0 0 20 20"><circle cx="10" cy="10" r="10" fill="var(--brand-green)"/><rect x="5" y="6.5" width="10" height="7" fill="none" stroke="#fff" stroke-width="1.2"/><path d="M5,6.5 L10,10.5 L15,6.5" fill="none" stroke="#fff" stroke-width="1.2"/></svg><span>info@<span class="accent">birchwoodam</span>.com</span></li>
      <li><svg viewBox="0 0 20 20"><circle cx="10" cy="10" r="10" fill="var(--brand-green)"/><g fill="none" stroke="#fff" stroke-width="1.1"><circle cx="10" cy="10" r="5"/><ellipse cx="10" cy="10" rx="2.2" ry="5"/><path d="M5,10 H15"/></g></svg><span>www.<span class="accent">birchwoodam</span>.com</span></li>
    </ul>
    <p class="address"><span class="address__label">Address:</span> 240 rue des Érables, Ville Mont-Clair, QC H2X 3K9</p>
  </section>

</main>
</body>
</html>
```